Company/Customer - Leave-Behind Card

Need a Standard size post card 4x6
Hard Stock Paper, Glossy
This will be a logo embossed card that is left behind with our customers
after work is completed, and also for potential customers with additional needs
You completed our Company design, for us,
We are Tandry Pane Studio LLC
I will upload logos and some info we need to have on th eproject
Target Market(s)
We are a professional company (Husband, Wife Team) specializing in Installation of premium Window fashions. Drapery, Shades, Blinds and custom window treatments.
We also specialize in project planning, Consultation, take down, put up services and will also provide some designing but are not specialists in the field. We can also take care of installing/hanging other items, such as Mirrors, paintings, etc...
We want to target both current customers, and potential customers for which leads will be generated
Industry/Entity Type
Professional Service
Font styles to use
Colors
Designer to choose colors to be used in the design.
Requirements
Must have
- Our company logo, our partner logos but not as prominent, our skill sets and certifications. Mission statement
Nice to have
- Eye catching colors, simple design, not to busy, or have to much to look at.
- I would like to see the logos embossed or maybe a looking glass effect.
Should not have
- Too busy, or too much to look at

```html
<!DOCTYPE html>
<html lang="en">
<head>
<meta charset="utf-8">
<title>Tandry Pane Studio LLC – Leave-Behind Card</title>
<link rel="stylesheet" href="https://fonts.googleapis.com/css2?family=Open+Sans:ital,wght@0,400;0,600;0,700;0,800;1,400&family=Cormorant+Garamond:ital@1&display=swap">
<style>
  :root {
    --navy: #1f2a6b;
    --blue: #2c5aa8;
    --blue-deep: #213f86;
    --sky: #3a8fd4;
    --ink: #111111;
    --white: #ffffff;
    --paper: #f3f4f6;
    --silver: #c9ccd1;
    --stage: #2a2a2a;
    --badge-orange: #e97d2a;
    --badge-grey: #8b8f95;
  }
  * { margin: 0; padding: 0; box-sizing: border-box; }
  html, body { width: 880px; height: 1200px; overflow: hidden; }
  body { background: var(--stage); font-family: "Open Sans", sans-serif; position: relative; }

  .card { position: absolute; left: 60px; width: 760px; height: 506px; overflow: hidden; background: var(--paper); }
  .card--front { top: 60px; }
  .card--back { top: 634px; }
  .card svg.art { position: absolute; inset: 0; width: 760px; height: 506px; }
  .abs { position: absolute; }

  /* front */
  .front__header { left: 0; top: 0; width: 760px; height: 142px; background: linear-gradient(90deg, #ffffff, #eceef1); }
  .front__band { left: 0; top: 142px; width: 760px; height: 266px; background: linear-gradient(90deg, var(--blue-deep), var(--blue)); }
  .front__footer { left: 0; top: 408px; width: 760px; height: 98px; background: linear-gradient(90deg, #ffffff, var(--silver)); }

  .brand { left: 52px; top: 56px; display: flex; align-items: center; gap: 10px; }
  .brand__mark { width: 26px; height: 26px; background: var(--blue); }
  .brand__name { font-weight: 700; font-size: 21px; line-height: 1.2; color: var(--navy); letter-spacing: 0.2px; white-space: nowrap; }
  .brand__tagline { left: 48px; top: 106px; font-family: "Cormorant Garamond", serif; font-style: italic; font-size: 11px; color: var(--blue); }

  .specialty { left: 44px; top: 154px; color: var(--white); width: 300px; }
  .specialty__title { font-weight: 800; font-size: 24px; line-height: 29px; letter-spacing: 0.3px; }
  .rule { height: 2px; background: var(--white); opacity: .85; }
  .specialty .rule { width: 130px; margin: 4px 0 8px; }
  .specialty__list { font-weight: 700; font-size: 18px; line-height: 24px; margin-left: 1px; }
  .specialty__sub { font-weight: 600; font-size: 15.5px; line-height: 21px; margin-top: 4px; }
  .specialty .rule--short { width: 150px; margin: 4px 0 5px; }
  .specialty__body { font-size: 14px; line-height: 20px; }

  .call { left: 48px; }
  .call__label { font-weight: 700; font-size: 22px; line-height: 1.3; letter-spacing: 0.3px; }
  .call__number { font-weight: 800; font-size: 46px; line-height: 1; letter-spacing: 0.5px; }
  .card--front .call { top: 420px; color: var(--navy); }
  .card--front .call__label { color: var(--ink); }

  /* back */
  .back__panel { left: 0; top: 0; width: 760px; height: 506px; background: linear-gradient(90deg, #ffffff, #e9ebee); }
  .about { left: 34px; top: 30px; width: 340px; }
  .about__title { font-weight: 800; font-size: 19.5px; color: var(--navy); letter-spacing: 0.3px; }
  .about .rule { width: 250px; margin: 8px 0 10px; background: var(--ink); opacity: 1; height: 1.5px; }
  .about__lead { font-weight: 700; font-size: 18px; color: var(--ink); }
  .about__text { font-size: 18px; line-height: 26px; color: var(--ink); }
  .about__mission { font-weight: 700; font-size: 18px; color: var(--blue); margin-top: 8px; }
  .about__body { font-size: 10.5px; line-height: 14.5px; color: var(--ink); margin-top: 4px; width: 270px; }

  .back__band { left: 0; top: 282px; width: 400px; height: 94px; background: linear-gradient(90deg, var(--blue-deep), var(--blue)); }
  .card--back .call { top: 292px; left: 34px; color: var(--white); }

  .partners { left: 34px; top: 392px; width: 290px; }
  .partners__badges { display: flex; gap: 14px; margin-bottom: 14px; }
  .badge { display: flex; align-items: center; gap: 8px; }
  .badge__disc { width: 34px; height: 34px; border-radius: 50%; background: var(--badge-orange); }
  .badge__plate { width: 96px; height: 26px; border-radius: 3px; background: var(--badge-grey); opacity: .55; }
  .partners__row { display: flex; align-items: center; gap: 14px; margin-bottom: 10px; }
  .partner-chip { height: 14px; border-radius: 2px; background: var(--badge-grey); opacity: .6; }
</style>
</head>
<body>

<section class="card card--front" aria-label="Card front">
  <div class="abs front__header"></div>
  <div class="abs front__band"></div>
  <div class="abs front__footer"></div>

  <svg class="art" viewBox="0 0 760 506">
    <defs>
      <linearGradient id="frontPhoto" x1="0" y1="0" x2="1" y2="1">
        <stop offset="0" stop-color="#3d4a52"/>
        <stop offset=".45" stop-color="#b9c6cf"/>
        <stop offset="1" stop-color="#2f3a40"/>
      </linearGradient>
      <linearGradient id="frontInsetA" x1="0" y1="0" x2="1" y2="1">
        <stop offset="0" stop-color="#dfe5ea"/>
        <stop offset="1" stop-color="#8a96a0"/>
      </linearGradient>
      <linearGradient id="frontInsetB" x1="0" y1="0" x2="1" y2="1">
        <stop offset="0" stop-color="#c9cfd4"/>
        <stop offset="1" stop-color="#7d8690"/>
      </linearGradient>
    </defs>
    <path d="M394 0 L414 0 C352 150 356 380 476 506 L448 506 C330 380 330 150 394 0 Z" fill="var(--sky)"/>
    <path d="M414 0 L760 0 L760 506 L476 506 C356 380 352 150 414 0 Z" fill="url(#frontPhoto)" role="img" aria-label="Photo of a modern room with sheer horizontal shades, pendant lights and a white pedestal table"/>
    <circle cx="380" cy="228" r="104" fill="url(#frontInsetA)" stroke="var(--navy)" stroke-width="7" role="img" aria-label="Photo of a bright room with sheer shades on large windows"/>
    <circle cx="414" cy="362" r="68" fill="url(#frontInsetB)" stroke="var(--navy)" stroke-width="7" role="img" aria-label="Photo of sheer shades over a sliding door"/>
  </svg>

  <div class="abs brand">
    <span class="brand__mark"></span>
    <span class="brand__name">Tandry Pane Studio LLC</span>
  </div>
  <p class="abs brand__tagline">Professional Installation Of Hard And Soft Window Treatments</p>

  <div class="abs specialty">
    <h2 class="specialty__title">SPECIALIZING IN</h2>
    <div class="rule"></div>
    <p class="specialty__list">INSTALL WINDOW<br>TREATMENTS.<br>SHUTTER, SHADES,<br>BLINDS, ETC...</p>
    <p class="specialty__sub">We also Specialize in</p>
    <div class="rule rule--short"></div>
    <p class="specialty__body">Project planning, Consultation,<br>Take down, Put up services and<br>will also provide some designing</p>
  </div>

  <div class="abs call">
    <p class="call__label">CALL US NOW</p>
    <p class="call__number">0123 456 789</p>
  </div>
</section>

<section class="card card--back" aria-label="Card back">
  <div class="abs back__panel"></div>
  <div class="abs back__band"></div>

  <svg class="art" viewBox="0 0 760 506">
    <defs>
      <linearGradient id="backPhoto" x1="0" y1="0" x2="1" y2="1">
        <stop offset="0" stop-color="#8a5a2b"/>
        <stop offset=".5" stop-color="#c98d45"/>
        <stop offset="1" stop-color="#4a2a18"/>
      </linearGradient>
      <linearGradient id="backInsetA" x1="0" y1="0" x2="1" y2="1">
        <stop offset="0" stop-color="#f1ede6"/>
        <stop offset="1" stop-color="#c7a774"/>
      </linearGradient>
      <linearGradient id="backInsetB" x1="0" y1="0" x2="1" y2="1">
        <stop offset="0" stop-color="#d9d7d3"/>
        <stop offset="1" stop-color="#8d8a84"/>
      </linearGradient>
    </defs>
    <path d="M350 0 L376 0 C470 120 470 400 314 506 L296 506 C440 400 444 120 350 0 Z" fill="var(--sky)"/>
    <path d="M376 0 L760 0 L760 506 L314 506 C470 400 470 120 376 0 Z" fill="url(#backPhoto)" role="img" aria-label="Photo of a wood-panelled study with woven roman shades, a chandelier, a desk and a patterned rug"/>
    <circle cx="412" cy="186" r="92" fill="url(#backInsetA)" stroke="var(--navy)" stroke-width="7" role="img" aria-label="Photo of a bay window with woven shades and a round table"/>
    <circle cx="412" cy="306" r="60" fill="url(#backInsetB)" stroke="var(--navy)" stroke-width="7" role="img" aria-label="Photo of a window with light wood blinds beside a lamp"/>
  </svg>

  <div class="abs about">
    <h2 class="about__title">FAMILY OWNED BUSINESS</h2>
    <div class="rule"></div>
    <p class="about__lead">We can also take care of</p>
    <p class="about__text">Installing/hanging other items,<br>such as Mirrors, paintings, etc...</p>
    <h3 class="about__mission">Mission statement</h3>
    <p class="about__body">Lorem ipsum dolor sit amet, consectetur adipiscing elit, sed do eiusmod tempor incididunt ut labore et dolore magna aliqua. Ut enim ad minim veniam, quis nostrud exercitation ullamco laboris nisi ut aliquip ex ea commodo consequat.</p>
  </div>

  <div class="abs call">
    <p class="call__label">CALL US NOW</p>
    <p class="call__number">0123 456 789</p>
  </div>

  <div class="abs partners" aria-label="Partner certifications">
    <div class="partners__badges">
      <div class="badge"><span class="badge__disc"></span><span class="badge__plate"></span></div>
      <div class="badge"><span class="badge__disc"></span><span class="badge__plate"></span></div>
    </div>
    <div class="partners__row">
      <span class="partner-chip" style="width:80px"></span>
      <span class="partner-chip" style="width:76px"></span>
      <span class="partner-chip" style="width:22px"></span>
    </div>
    <div class="partners__row">
      <span class="partner-chip" style="width:40px"></span>
      <span class="partner-chip" style="width:36px"></span>
      <span class="partner-chip" style="width:56px"></span>
      <span class="partner-chip" style="width:38px"></span>
    </div>
  </div>
</section>

</body>
</html>
```